TLPB Business Card Design

Business card for sole operator professional civil and traffic engineer.
Clients are developers and planners who require assistance with traffic strategic master planning advice and design development for access and infrastructure associated with the development.
Colours already in use are greens for the business name and black for other legend. The attached file shows the letterhead template which is currently in use.
Target Market(s)
Professional Clients in development industry
Most clients known to the Principal and card is mostly required to allow ongoing contact
Industry/Entity Type
Business
Contact Information for Business Card
DESMOND HALVERTON CONSULTING SERVICES
ABN 37 818 502 194
PO Box 871 KERRAWAY NSW 2619
Desmond Halverton 0431 558 906
desmond.halverton@quillmarsh.net

```html
<!DOCTYPE html>
<html lang="en">
<head>
<meta charset="utf-8">
<title>Desmond Halverton Consulting Services – Business Card</title>
<link href="https://fonts.googleapis.com/css2?family=Lato:wght@400;700&display=swap" rel="stylesheet">
<style>
  :root {
    --page-bg: #eeeeea;
    --card-black: #1c1d1c;
    --brand-green: #8dc63f;
    --band-line: #e6f0cf;
    --text-green: #9ccf45;
  }
  html, body {
    margin: 0;
    padding: 0;
    width: 1200px;
    height: 841px;
    overflow: hidden;
    background: var(--page-bg);
    font-family: "Lato", Arial, sans-serif;
  }
  .stage {
    width: 1200px;
    height: 841px;
    display: flex;
    align-items: center;
    justify-content: center;
  }
  .card {
    position: relative;
    width: 1000px;
    height: 606px;
    background: var(--brand-green);
    box-shadow: 0 6px 24px rgba(0,0,0,0.18);
    overflow: hidden;
  }
  .card__band-top {
    position: absolute;
    left: 0; top: 0;
    width: 100%; height: 80px;
    background: var(--brand-green);
  }
  .card__panel {
    position: absolute;
    left: 0; top: 80px;
    width: 100%; height: 348px;
    box-sizing: border-box;
    background: var(--card-black);
    border-top: 8px solid var(--band-line);
    border-bottom: 8px solid var(--band-line);
    display: flex;
    flex-direction: column;
    align-items: center;
    justify-content: center;
    color: var(--text-green);
    text-align: center;
  }
  .card__band-bottom {
    position: absolute;
    left: 0; bottom: 0;
    width: 100%; height: 178px;
    background: var(--brand-green);
  }
  .business-name {
    font-weight: 700;
    font-size: 36px;
    letter-spacing: 0.2px;
    margin: 0 0 6px;
  }
  .business-abn,
  .business-address {
    font-weight: 700;
    font-size: 27px;
    margin: 0 0 2px;
  }
  .principal-name {
    font-size: 44px;
    margin: 22px 0 10px;
    font-weight: 400;
  }
  .principal-name strong { font-weight: 700; }
  .contact-line {
    font-size: 25px;
    margin: 0;
  }
  .contact-line .label { font-weight: 700; }
  .contact-line .divider { margin: 0 10px; }
</style>
</head>
<body>
  <main class="stage">
    <article class="card">
      <div class="card__band-top"></div>
      <section class="card__panel">
        <h1 class="business-name">DESMOND HALVERTON CONSULTING SERVICES</h1>
        <p class="business-abn">ABN 37 818 502 194</p>
        <p class="business-address">PO Box 871 KERRAWAY NSW 2619</p>
        <p class="principal-name">DESMOND <strong>HALVERTON</strong></p>
        <p class="contact-line">
          <span class="label">PHONE:</span> 0431 558 906
          <span class="divider">|</span>
          <span class="label">EMAIL:</span> desmond.halverton@quillmarsh.net
        </p>
      </section>
      <div class="card__band-bottom"></div>
    </article>
  </main>
</body>
</html>
```